San Francisco Hotel in need of banner ad set

We need a banner ad set for our new hotel in San Francisco called 'The Marlowe Larkspur'. The Marlowe Larkspur is joining our 'Thistledown Lodging' portfolio of hotels. The final design should communicate 'Now a Piece of Thistledown Lodging' and our introductory 15% discount.

Here are the details of the promotion:

http://mrlw.preview.vexolint.example/promotions/welcome-to-thistledown-lodging.htm

Ads are fixed (no flash, no animation)

Ad Dimensions:
120x120
160x600
300x250
728x90

Target Market(s)

Customers who have researched rates on our website and plan to travel to San Francisco. These ads will remarket our hotel to them after leaving our site.

Industry/Entity Type

Hotel

Font styles to use
Serif

Colors
ec1f27
faee3f

Requirements
Must have
• Check Availability button
The Marlowe Larkspur logo (attached both black and white depending on what you need)
Thistledown Lodging logo
15% Off

Sub text:
No up front charges
24 hour cancellations
Nice to have
• No up front charges
24 hour cancellations

```html
<!DOCTYPE html>
<html lang="en">
<head>
<meta charset="utf-8">
<title>The Marlowe Larkspur – Banner Ad Set</title>
<link rel="stylesheet" href="https://fonts.googleapis.com/css2?family=Open+Sans:wdth,wght@75..100,300..800&display=swap">
<style>
  :root {
    --red: #ec1f27;
    --yellow: #faee3f;
    --btn-top: #ffe23a;
    --btn-bottom: #f3a600;
    --ink: #1d1d1d;
    --white: #ffffff;
    --strip-top: #ffffff;
    --strip-bottom: #e9e6e6;
    --backdrop: #3b1b0d;
    --sky: #6f9fcc;
    --facade: #e7e1d6;
    --street: #4a4646;
  }
  * { margin: 0; padding: 0; box-sizing: border-box; }
  html, body { width: 1200px; height: 801px; overflow: hidden; background: var(--backdrop); }
  body { font-family: "Open Sans", Arial, sans-serif; position: relative; }

  .ad { position: absolute; overflow: hidden; transform-origin: 0 0; transform: scale(1.1811); background: var(--red); color: var(--white); font-stretch: 75%; text-align: center; }
  .ad--sky { left: 54px; top: 44px; width: 160px; height: 600px; }
  .ad--leader { left: 266px; top: 44px; width: 728px; height: 90px; }
  .ad--rect { left: 266px; top: 171px; width: 300px; height: 250px; }
  .ad--square { left: 267px; top: 484px; width: 120px; height: 120px; }

  .brand { font-weight: 600; font-stretch: 87.5%; color: var(--white); line-height: 1; letter-spacing: 0.2px; }
  .brand--dark { color: var(--ink); }

  .headline { font-weight: 700; text-transform: uppercase; line-height: 1.05; }
  .tagline { font-weight: 700; text-transform: uppercase; line-height: 1.2; }
  .offer { font-weight: 800; line-height: 1; }
  .offer-sub { font-weight: 400; text-transform: uppercase; line-height: 1; }

  .cta { position: absolute; display: flex; align-items: center; justify-content: center; gap: 6px;
         background: linear-gradient(var(--btn-top), var(--btn-bottom)); border: 1px solid #c98700; border-radius: 3px;
         color: var(--ink); font-weight: 600; font-size: 13px; box-shadow: 0 1px 2px rgba(0,0,0,.35); }
  .cta svg { width: 15px; height: 15px; }

  .terms { position: absolute; background: linear-gradient(var(--strip-top), var(--strip-bottom)); color: var(--ink);
           font-stretch: 87.5%; font-size: 11px; line-height: 1.35; display: flex; align-items: center; justify-content: center; gap: 16px; }
  .terms li { list-style: none; }
  .terms--bulleted li::before { content: "•"; margin-right: 6px; }

  .partner-badge { position: absolute; border-radius: 50%; background: var(--white); border: 2px solid var(--yellow); }

  .abs { position: absolute; }
  .photo { display: block; position: absolute; }
</style>
</head>
<body>

<!-- 160 x 600 -->
<section class="ad ad--sky" aria-label="160 by 600 banner">
  <p class="brand abs" style="left:0;right:0;top:17px;font-size:17px;">The Marlowe Larkspur</p>
  <svg class="photo" style="left:0;top:50px" width="160" height="265" viewBox="0 0 160 265">
    <defs>
      <linearGradient id="skyShot" x1="0" y1="0" x2="0" y2="1">
        <stop offset="0" stop-color="var(--sky)"/><stop offset=".25" stop-color="var(--facade)"/>
        <stop offset=".8" stop-color="#cfc6b8"/><stop offset="1" stop-color="var(--street)"/>
      </linearGradient>
    </defs>
    <path role="img" aria-label="Photo of the hotel's white corner building on a downtown street" d="M0 0H160V238Q80 275 0 238Z" fill="url(#skyShot)"/>
    <path d="M0 238Q80 275 0 238M0 240Q80 276 160 240" fill="none" stroke="var(--yellow)" stroke-width="4"/>
  </svg>
  <p class="headline abs" style="left:0;right:0;top:329px;font-size:19px;">Downtown<br>San Francisco</p>
  <p class="tagline abs" style="left:0;right:0;top:374px;font-size:12px;">Now a piece of<br>Thistledown Lodging</p>
  <span class="partner-badge" style="left:63px;top:412px;width:34px;height:34px;"></span>
  <p class="offer abs" style="left:0;right:0;top:462px;font-size:29px;">15% OFF</p>
  <p class="offer-sub abs" style="left:0;right:0;top:491px;font-size:21px;">Room Rates</p>
  <a class="cta" style="left:13px;top:524px;width:134px;height:26px;">Check Availability
    <svg viewBox="0 0 16 16"><circle cx="8" cy="8" r="8" fill="var(--ink)"/><path d="M6.5 4.5 10 8 6.5 11.5" fill="none" stroke="var(--white)" stroke-width="2"/></svg></a>
  <ul class="terms" style="left:0;top:560px;width:160px;height:40px;flex-direction:column;gap:0;">
    <li>No up front charges</li><li>24 hour cancellations</li>
  </ul>
</section>

<!-- 728 x 90 -->
<section class="ad ad--leader" aria-label="728 by 90 banner">
  <p class="brand abs" style="left:0;width:160px;top:19px;font-size:16px;">The Marlowe Larkspur</p>
  <a class="cta" style="left:12px;top:56px;width:134px;height:25px;">Check Availability
    <svg viewBox="0 0 16 16"><circle cx="8" cy="8" r="8" fill="var(--ink)"/><path d="M6.5 4.5 10 8 6.5 11.5" fill="none" stroke="var(--white)" stroke-width="2"/></svg></a>
  <svg class="photo" style="left:161px;top:0" width="310" height="70" viewBox="0 0 310 70">
    <defs>
      <linearGradient id="leaderShot" x1="0" y1="0" x2="0" y2="1">
        <stop offset="0" stop-color="#d9d4cb"/><stop offset=".6" stop-color="#8d857c"/><stop offset="1" stop-color="var(--street)"/>
      </linearGradient>
    </defs>
    <path role="img" aria-label="Photo of the hotel entrance and street corner" d="M0 0H296Q312 35 296 70H0Z" fill="url(#leaderShot)"/>
    <path d="M296 0Q312 35 296 70" fill="none" stroke="var(--yellow)" stroke-width="4"/>
  </svg>
  <span class="partner-badge" style="left:397px;top:16px;width:36px;height:36px;"></span>
  <ul class="terms terms--bulleted" style="left:161px;top:70px;width:303px;height:20px;">
    <li>No up front charges</li><li>24 hour cancellations</li>
  </ul>
  <p class="headline abs" style="left:465px;width:263px;top:9px;font-size:18px;">Downtown San Francisco</p>
  <p class="tagline abs" style="left:465px;width:263px;top:30px;font-size:12px;">Now a piece of Thistledown Lodging</p>
  <p class="offer abs" style="left:465px;width:263px;top:59px;font-size:20px;">15% OFF ROOM RATES</p>
</section>

<!-- 300 x 250 -->
<section class="ad ad--rect" aria-label="300 by 250 banner">
  <svg class="photo" style="left:0;top:0" width="160" height="225" viewBox="0 0 160 225">
    <defs>
      <linearGradient id="rectShot" x1="0" y1="0" x2="0" y2="1">
        <stop offset="0" stop-color="var(--sky)"/><stop offset=".2" stop-color="var(--facade)"/>
        <stop offset=".8" stop-color="#cbc2b4"/><stop offset="1" stop-color="var(--street)"/>
      </linearGradient>
    </defs>
    <path role="img" aria-label="Photo of the hotel's white corner building" d="M0 0H124Q160 110 146 225H0Z" fill="url(#rectShot)"/>
    <path d="M124 0Q160 110 146 225" fill="none" stroke="var(--yellow)" stroke-width="4"/>
  </svg>
  <p class="brand abs" style="left:148px;width:152px;top:20px;font-size:16px;">The Marlowe Larkspur</p>
  <span class="partner-badge" style="left:120px;top:95px;width:30px;height:30px;"></span>
  <p class="headline abs" style="left:150px;width:150px;top:58px;font-size:17px;">Downtown<br>San Francisco</p>
  <p class="tagline abs" style="left:150px;width:150px;top:97px;font-size:12px;">Now a piece of<br>Thistledown Lodging</p>
  <p class="offer abs" style="left:150px;width:150px;top:137px;font-size:27px;">15% OFF</p>
  <p class="offer-sub abs" style="left:150px;width:150px;top:164px;font-size:20px;">Room Rates</p>
  <a class="cta" style="left:157px;top:196px;width:134px;height:26px;">Check Availability
    <svg viewBox="0 0 16 16"><circle cx="8" cy="8" r="8" fill="var(--ink)"/><path d="M6.5 4.5 10 8 6.5 11.5" fill="none" stroke="var(--white)" stroke-width="2"/></svg></a>
  <ul class="terms terms--bulleted" style="left:0;top:226px;width:300px;height:24px;">
    <li>No up front charges</li><li>24 hour cancellations</li>
  </ul>
</section>

<!-- 120 x 120 -->
<section class="ad ad--square" aria-label="120 by 120 banner">
  <div class="abs" style="left:0;top:0;width:120px;height:38px;background:var(--white);"></div>
  <p class="brand brand--dark abs" style="left:0;right:0;top:13px;font-size:12px;">The Marlowe Larkspur</p>
  <div class="abs" style="left:0;top:38px;width:120px;height:3px;background:var(--yellow);"></div>
  <p class="tagline abs" style="left:0;right:0;top:45px;font-size:10px;">Now a piece of<br>Thistledown Lodging</p>
  <svg class="photo" style="left:0;top:72px" width="120" height="48" viewBox="0 0 120 48">
    <defs>
      <linearGradient id="squareShot" x1="0" y1="0" x2="0" y2="1">
        <stop offset="0" stop-color="#9c958c"/><stop offset="1" stop-color="var(--street)"/>
      </linearGradient>
    </defs>
    <rect role="img" aria-label="Photo of the hotel street frontage" width="120" height="48" fill="url(#squareShot)"/>
  </svg>
  <p class="offer abs" style="left:0;right:0;top:78px;font-size:18px;">15% OFF</p>
  <p class="offer-sub abs" style="left:0;right:0;top:97px;font-size:13px;font-weight:700;">Room Rates</p>
</section>

</body>
</html>
```